New Business Card Design for Manufacturing

We are an engineering/manufacturing company that offers Advanced machining/assembly/engineering services, as well as innovative products for the heavy duty engine cooling markets.

We are looking to get a new business card designed that is clean and modern looking, but still fits the wide range of technical/skilled work we do.

- We hope to use this design as the base for other design work in new Presentations, web, and print work.

Industry/Entity Type

Engineering

Contact Information for Business Card

Our preferred color of blue is (RGB) 22/71/159 but can vary slightly from that color. Our content will be our Logo and full company name (Fabricated Tooling Works, Inc.), company address, name, job title, phone number with extension, cell number, fax number, website, and email address on the cards.
We'd like the full company name next to the logo, but we are open to other interpretations of that layout.
Preferably, we would like the back side to be clean with just our logo, and the front to contain all of the contact information.

Colors
2f74b4
0355a3
85abd2

Requirements
Must have
• - Logo, company name, needed content - We are open to interpretation beyond that.
• - Standard size business card.
• - Horizontal orientation.
• - Enough space for lengthy names / job titles (for example, a job title could read "Directory of Human Resources" or "V.P. of Governmental Affairs"). We need this to look clean, whether the title be short (CEO) or long (as described above).

```html
<!DOCTYPE html>
<html lang="en">
<head>
<meta charset="utf-8">
<title>Fabricated Tooling Works – Business Card</title>
<link href="https://fonts.googleapis.com/css2?family=Lato:wght@400;700;900&display=swap" rel="stylesheet">
<style>
  :root{
    --brand-blue:#0355a3;
    --brand-blue-deep:#16479f;
    --ink:#1b1b1b;
    --paper:#ffffff;
    --stage:#3b3b3b;
  }
  *{margin:0;padding:0;box-sizing:border-box}
  html,body{width:1200px;height:1200px;overflow:hidden;background:var(--stage)}
  body{position:relative;font-family:"Lato",sans-serif}

  .card{position:absolute;width:700px;height:400px;overflow:hidden}

  /* back side */
  .card-back{left:90px;top:150px;background:var(--brand-blue);color:var(--paper)}
  .card-back .wordmark{position:absolute;left:0;right:0;top:120px;text-align:center;
    font-weight:900;font-size:120px;letter-spacing:6px;line-height:1}
  .card-back .tagline{position:absolute;left:0;right:0;top:250px;text-align:center;
    font-weight:900;font-size:28px;letter-spacing:3px;text-transform:uppercase}
  .card-back .web{position:absolute;left:0;right:0;bottom:40px;text-align:center;
    font-size:18px;letter-spacing:2px}

  /* front side */
  .card-front{left:410px;top:640px;background:var(--paper);color:var(--ink)}
  .card-front .band{position:absolute;left:0;right:0;bottom:0;height:14px;background:var(--brand-blue)}
  .brand{position:absolute;left:42px;top:44px;display:flex;align-items:flex-start;gap:18px}
  .brand .wordmark{font-weight:900;font-size:78px;letter-spacing:3px;color:var(--brand-blue);line-height:.9}
  .brand .tagline{font-weight:900;font-size:15px;letter-spacing:1.5px;color:var(--brand-blue);text-transform:uppercase;margin-top:6px}
  .brand .company{font-weight:900;font-size:21px;line-height:1.02;text-transform:uppercase;margin-top:2px}
  .brand .company small{font-size:10px;vertical-align:top}

  .person{position:absolute;left:42px;top:270px}
  .person .name{font-weight:700;font-size:30px;color:var(--brand-blue);text-transform:uppercase;letter-spacing:.5px}
  .person .title{font-size:21px;margin-top:2px}

  .contact{position:absolute;left:430px;top:150px;font-size:18px;line-height:1.25}
  .contact .address{margin-bottom:10px}
  .contact ul{list-style:none}
  .contact li{display:flex;align-items:center;gap:10px;height:25px}
  .contact svg{width:16px;height:16px;fill:var(--brand-blue);flex:none}
</style>
</head>
<body>

<section class="card card-back" aria-label="Card back">
  <div class="wordmark">FTW</div>
  <div class="tagline">Built to Endure</div>
  <div class="web">www.fabtoolworks.com</div>
</section>

<section class="card card-front" aria-label="Card front">
  <div class="brand">
    <div>
      <div class="wordmark">FTW</div>
      <div class="tagline">Built to Endure</div>
    </div>
    <div class="company">Fabricated<br>Tooling<br>Works <small>Inc</small></div>
  </div>

  <div class="person">
    <div class="name">Daniel Prescott</div>
    <div class="title">Directory of Human Resources</div>
  </div>

  <div class="contact">
    <div class="address">418 Alder Court<br>Houston, TX 77041</div>
    <ul>
      <li><svg viewBox="0 0 16 16"><path d="M3 1l3 3-1.5 2c1 2 3 4 5 5l2-1.5 3 3-2 2C7 14 2 9 1 3z"/></svg>512 555 0140</li>
      <li><svg viewBox="0 0 16 16"><path d="M4 0h8a1 1 0 0 1 1 1v14a1 1 0 0 1-1 1H4a1 1 0 0 1-1-1V1a1 1 0 0 1 1-1zm1 2v10h6V2zm3 11a1 1 0 1 0 0 2 1 1 0 0 0 0-2z"/></svg>512 555 0141</li>
      <li><svg viewBox="0 0 16 16"><path d="M4 1h8v4H4zM1 6h14v6h-2v3H3v-3H1zm4 4v4h6v-4z"/></svg>512 555 0143</li>
      <li><svg viewBox="0 0 16 16"><path d="M1 3h14v10H1zm1.5 1.5L8 9l5.5-4.5V4h-11z"/></svg>info@fabtoolworks.com</li>
      <li><svg viewBox="0 0 16 16"><path d="M8 0a8 8 0 1 0 0 16A8 8 0 0 0 8 0zm-1 1.6C5.7 3 5 5 5 7H1.6A6.5 6.5 0 0 1 7 1.6zM9 1.6A6.5 6.5 0 0 1 14.4 7H11c0-2-.7-4-2-5.4zM6.5 7c0-2 .6-3.7 1.5-4.8.9 1.1 1.5 2.8 1.5 4.8zM1.6 9H5c0 2 .7 4 2 5.4A6.5 6.5 0 0 1 1.6 9zm4.9 0h3c0 2-.6 3.7-1.5 4.8C7.1 12.7 6.5 11 6.5 9zM11 9h3.4A6.5 6.5 0 0 1 9 14.4c1.3-1.4 2-3.4 2-5.4z"/></svg>www.fabtoolworks.com</li>
    </ul>
  </div>

  <div class="band"></div>
</section>

</body>
</html>
```